Kelvara Advisory Corporate Brochure

Kelvara Advisory is a management consulting firm.

We need a corporate brochure showcasing our methodologies (two process diagrams) and our leadership team.

We would like it to look corporate, professional, clean and contemporary.

Happy to have duo tones using our Kelvara logo colours or mono pics.

Also like texture and 3 dimensional backgrounds and graphics.

We are waiting for head and shoulder photos of a couple of our Associate Directors (can you use placeholders while we obtain these please?)

Our web site is:

www.kelvaraadvisory.example.com.au

Thanks for your ideas.

Industry/Entity Type

Management Consulting

```html
<!DOCTYPE html>
<html lang="en">
<head>
<meta charset="utf-8">
<title>Why Kelvara Advisory</title>
<link href="https://fonts.googleapis.com/css2?family=PT+Sans:ital,wght@0,400;0,700;1,400&display=swap" rel="stylesheet">
<style>
  :root {
    --maroon: #6b0c10;
    --maroon-deep: #5a0a0d;
    --teal: #1f6f7d;
    --teal-dark: #1b5f6b;
    --teal-pale: #b9dde2;
    --grey-box: #8a8a8c;
    --ink: #1c1c1c;
    --black: #0d0d0d;
    --stripe: #9a9a9a;
    --white: #ffffff;
  }
  * { box-sizing: border-box; margin: 0; padding: 0; }
  html, body { width: 927px; height: 1200px; overflow: hidden; background: var(--white); }
  body { font-family: "PT Sans", Arial, sans-serif; color: var(--ink); }

  .page { position: relative; width: 927px; height: 1200px; overflow: hidden; background: var(--white); }

  .backdrop {
    position: absolute; left: 152px; top: 0; width: 775px; height: 1200px;
    background:
      linear-gradient(115deg, rgba(255,255,255,0) 40%, rgba(200,222,228,.55) 55%, rgba(255,255,255,0) 70%),
      linear-gradient(180deg, #f4f7f8 0%, #dfe9ec 45%, #eef2f3 70%, #c9d6da 100%);
  }

  .side-strip { position: absolute; left: 0; top: 0; width: 152px; height: 1200px; background: var(--black); }
  .side-strip svg { position: absolute; left: 0; top: 0; }
  .brand {
    position: absolute; left: 22px; top: 1090px; width: 120px;
    color: var(--white); font-size: 22px; font-weight: 400; line-height: 1.1;
  }
  .brand-dot { display: block; width: 26px; height: 26px; border-radius: 50%; background: var(--teal); margin-bottom: 10px; }

  .title-bar {
    position: absolute; left: 156px; top: 30px; width: 432px; height: 64px;
    background: var(--maroon); box-shadow: 3px 4px 8px rgba(0,0,0,.35);
    color: var(--white); font-size: 33px; font-weight: 400; line-height: 64px; padding-left: 24px;
  }

  .intro {
    position: absolute; left: 179px; top: 126px; width: 720px;
    font-size: 24px; line-height: 33px;
  }
  .enablers { position: absolute; left: 179px; top: 292px; width: 680px; list-style: none; font-size: 24px; line-height: 31px; }
  .enablers li { position: relative; padding-left: 56px; }
  .enablers li::before {
    content: ""; position: absolute; left: 2px; top: 8px; width: 12px; height: 15px;
    border: 1.5px solid var(--ink);
  }

  .framework {
    position: absolute; left: 224px; top: 520px; width: 640px; height: 356px;
    background: var(--white); box-shadow: 4px 5px 14px rgba(0,0,0,.35);
  }
  .framework > div { position: absolute; display: flex; align-items: center; justify-content: center; text-align: center; font-weight: 700; }
  .fw-head { left: 123px; top: 18px; width: 395px; height: 42px; background: var(--teal-dark); color: var(--white); font-size: 12px; line-height: 13px; }
  .fw-head span { width: 25%; }
  .fw-existing { left: 26px; top: 80px; width: 98px; height: 162px; background: var(--maroon); color: var(--white); font-size: 13px; line-height: 15px; }
  .fw-future { left: 518px; top: 80px; width: 98px; height: 162px; background: var(--teal); color: var(--white); font-size: 10px; line-height: 13px; }
  .fw-cell { background: var(--grey-box); color: var(--white); font-size: 10px; line-height: 12px; padding: 2px; }
  .fw-outcome { background: var(--white); border: 1.5px solid var(--maroon); color: var(--ink); font-size: 10px; line-height: 12px; }
  .fw-lever { background: var(--teal-pale); color: var(--teal-dark); font-size: 10px; line-height: 12px; }

  .quote {
    position: absolute; left: 473px; top: 995px; width: 454px; height: 156px;
    background: var(--maroon-deep); color: var(--white);
    font-style: italic; font-size: 16px; line-height: 20px; text-align: center;
    padding: 22px 12px 0 50px;
  }
</style>
</head>
<body>
<main class="page">
  <div class="backdrop" role="img" aria-label="Soft blue-grey architectural 3D background"></div>

  <aside class="side-strip">
    <svg width="152" height="1200" viewBox="0 0 152 1200" aria-hidden="true">
      <g fill="var(--stripe)">
        <rect x="70" y="0" width="8" height="1040"/>
        <rect x="86" y="0" width="4" height="1040" fill="#e6e6e6"/>
        <rect x="98" y="0" width="8" height="1040"/>
        <rect x="114" y="0" width="3" height="1040" fill="#e6e6e6"/>
        <rect x="124" y="0" width="6" height="1040"/>
        <rect x="138" y="0" width="3" height="1040" fill="#e6e6e6"/>
      </g>
    </svg>
    <div class="brand"><span class="brand-dot"></span>Kelvara<br>Advisory</div>
  </aside>

  <h1 class="title-bar">WHY Kelvara advisory?</h1>

  <p class="intro">With over 30 years experience of developing more effective business processes and strategy for our clients through our VECTA program, Kelvara achieves dramatic improvements for clients across all value drivers by focusing on four key enablers.</p>

  <ul class="enablers">
    <li>Systems that enable consistent execution of strategy;</li>
    <li>Processes that are optimised for customers and staff;</li>
    <li>Employees that are empowered and engaged; and</li>
    <li>Channel strategies that engage and meet the needs of customers.</li>
  </ul>

  <section class="framework" aria-label="VECTA framework">
    <div class="fw-head"><span>Systems</span><span>Processes<br>&amp; Practices</span><span>Empowered<br>Employees</span><span>Customers<br>&amp; Channels</span></div>
    <div class="fw-existing">Existing<br>Organization<br>and<br>Processes</div>

    <div class="fw-cell" style="left:152px;top:80px;width:80px;height:162px;">Optimisation &amp; Exploitation of Systems and Technology</div>
    <div class="fw-cell" style="left:240px;top:80px;width:78px;height:162px;">Identifying &amp; Delivering Better Practice Blueprints</div>
    <div class="fw-cell" style="left:327px;top:80px;width:82px;height:49px;">People Culture Engagement</div>
    <div class="fw-cell" style="left:327px;top:135px;width:82px;height:52px;">Effective Training &amp; Development</div>
    <div class="fw-cell" style="left:327px;top:193px;width:82px;height:49px;">Org Structure Mgt Practices</div>
    <div class="fw-cell" style="left:415px;top:80px;width:79px;height:49px;">Customers and Markets</div>
    <div class="fw-cell" style="left:415px;top:135px;width:79px;height:52px;">Products &amp; Services</div>
    <div class="fw-cell" style="left:415px;top:193px;width:79px;height:49px;">Delivery Channels</div>

    <div class="fw-future">DESIRED FUTURE STATE<br><br>ORGANISATION AND PROCESSES</div>

    <div class="fw-outcome" style="left:152px;top:253px;width:80px;height:45px;">Systems<br>that Enable</div>
    <div class="fw-outcome" style="left:240px;top:253px;width:78px;height:45px;">Processes to Empower &amp; Engage</div>
    <div class="fw-outcome" style="left:327px;top:253px;width:82px;height:45px;">Employees<br>that can<br>Execute</div>
    <div class="fw-outcome" style="left:415px;top:253px;width:79px;height:45px;">Customers<br>that will<br>Embrace</div>

    <div class="fw-lever" style="left:152px;top:309px;width:166px;height:30px;">Enabling Levers</div>
    <div class="fw-lever" style="left:327px;top:309px;width:82px;height:30px;">People<br>Levers</div>
    <div class="fw-lever" style="left:415px;top:309px;width:79px;height:30px;">Strategic<br>Levers</div>
  </section>

  <blockquote class="quote">“Delivering efficiency gains as high as 20% may<br>seem far-fetched, but that is what<br>we have achieved…<br>again and again”</blockquote>
</main>
</body>
</html>
```